依頼詳細
サイズが決まっています。添付データのサイズを参照してください。
モルテナカタログのような感じのデザインをお願いします。
記載項目
日常生活に支援が必要な方、支援をする方へ『あんしん』をお届けします。

使いやすい、見やすい、分かりやすい
希望イメージ
シンプル 複雑
単色 カラフル
暗い 明るい
日常 高級
遊び心 厳粛
未来的 伝統的
女性的 男性的
希望する色
青系、緑系
納品ファイル
• イラストレーター形式 (.ai)
補足説明
”カタログの表紙を別刷り”というのは
添付したSOFT ROAD の下のオレンジの枠内を差し替えるということです。
依頼内容が分かりにくいようで失礼いたしました。
■ 選んだ理由

今回、当カタログの取り扱い品目と安心を届けるというコンセプトに合致している点、そして社内での投票をさせて頂きました結果、korumi様のご提案を採用させて戴きました。

■ 提案者全員のお礼・コメント

今度は本当に沢山のご提案をいただきまして有難うございました。
どのランサーの方の提案も素晴らしいものばかりでしたが、
上記理由により、社内で最も票の多かった提案を採用させて頂きました。

```html
<!DOCTYPE html>
<html lang="ja">
<head>
<meta charset="utf-8">
<title>SOFT ROAD 福祉用具総合カタログ</title>
<link rel="stylesheet" href="https://fonts.googleapis.com/css2?family=M+PLUS+Rounded+1c:wght@500;700;800&family=Oswald:wght@500&family=Noto+Sans+JP:wght@500;700&display=swap">
<style>
  :root {
    --paper: #ffffff;
    --title-red: #e6414b;
    --panel-green: #b9d86d;
    --circle-cream: #fffbe3;
    --town-green: #8cbf45;
    --town-warm: #f2c46b;
    --accent-orange: #f08a2a;
    --anshin-teal: #2fb3c4;
    --ink: #333333;
    --ink-soft: #555555;
  }
  * { margin: 0; padding: 0; box-sizing: border-box; }
  html, body { width: 848px; height: 1200px; overflow: hidden; background: var(--paper); }
  .cover {
    position: relative;
    width: 848px;
    height: 1200px;
    background: var(--paper);
    font-family: "M PLUS Rounded 1c", sans-serif;
    color: var(--ink);
  }
  .catalog-label {
    position: absolute; top: 30px; left: 0; width: 100%;
    text-align: center; font-size: 32px; font-weight: 700;
    color: var(--title-red); letter-spacing: 2px;
  }
  .brand-title {
    position: absolute; top: 82px; left: 0; width: 100%;
    text-align: center; font-family: "Oswald", sans-serif;
    font-weight: 500; font-size: 150px; line-height: 1;
    color: var(--title-red); letter-spacing: 14px;
  }
  .tagline {
    position: absolute; top: 250px; left: 0; width: 100%;
    text-align: center; font-family: "Noto Sans JP", sans-serif;
    font-size: 17px; font-weight: 500; color: var(--ink-soft); letter-spacing: 1px;
  }
  .panel {
    position: absolute; top: 283px; left: 62px;
    width: 724px; height: 838px;
    background: var(--panel-green);
    overflow: hidden;
  }
  .panel-art { position: absolute; inset: 0; }
  .item-illust { position: absolute; border-radius: 18px; opacity: .55; }
  .item-walker { left: 20px; top: 18px; width: 120px; height: 100px; background: linear-gradient(#d9dde0, #9aa3aa); }
  .item-cane { left: 606px; top: 14px; width: 100px; height: 108px; background: linear-gradient(135deg, #e6b07a, #c26d3a); }
  .item-bed { left: 22px; top: 640px; width: 150px; height: 120px; background: linear-gradient(#fbe8d0, #e0b88d); }
  .item-wheelchair { left: 570px; top: 610px; width: 135px; height: 150px; background: linear-gradient(#6f86c9, #2a3f86); }
  .message {
    position: absolute; left: 0; width: 100%; text-align: center;
  }
  .message-lead { top: 290px; font-size: 29px; font-weight: 700; line-height: 1.55; }
  .anshin-row { top: 440px; display: flex; justify-content: center; align-items: flex-end; gap: 6px; }
  .anshin-char {
    display: inline-flex; align-items: center; justify-content: center;
    width: 62px; height: 66px; border-radius: 20px;
    background: var(--anshin-teal); color: #fff;
    font-size: 46px; font-weight: 800;
  }
  .anshin-particle { font-size: 30px; font-weight: 700; margin-left: 6px; }
  .message-close { top: 522px; font-size: 28px; font-weight: 700; }
  .people-illust {
    position: absolute; left: 232px; top: 580px; width: 260px; height: 100px;
    border-radius: 50px 50px 20px 20px;
    background: linear-gradient(#f7d9b9, #e7b98c);
  }
  .maker {
    position: absolute; top: 1140px; left: 0; width: 100%;
    display: flex; justify-content: center; align-items: center; gap: 14px;
    font-family: "Noto Sans JP", sans-serif; font-size: 30px; font-weight: 700; color: var(--ink);
  }
  .maker-mark { width: 34px; height: 34px; border-radius: 50%; border: 3px solid var(--ink); }
</style>
</head>
<body>
<main class="cover">
  <p class="catalog-label">福祉用具総合カタログ</p>
  <h1 class="brand-title">SOFT ROAD</h1>
  <p class="tagline">FOR GOOD HAPPINESS HUMAN LIFE</p>

  <section class="panel">
    <svg class="panel-art" width="724" height="838" viewBox="0 0 724 838">
      <defs>
        <linearGradient id="townTone" x1="0" y1="0" x2="1" y2="1">
          <stop offset="0" stop-color="var(--town-green)"/>
          <stop offset=".5" stop-color="var(--town-warm)"/>
          <stop offset="1" stop-color="var(--town-green)"/>
        </linearGradient>
        <path id="sloganArc" d="M 63 228 A 345 345 0 0 1 661 228"/>
      </defs>
      <circle cx="362" cy="400" r="290" fill="none" stroke="url(#townTone)" stroke-width="80" opacity=".8" role="img" aria-label="円形に並ぶ家と木の街並みイラスト"/>
      <circle cx="362" cy="400" r="250" fill="var(--circle-cream)"/>
      <text font-family="M PLUS Rounded 1c, sans-serif" font-size="28" font-weight="700" fill="var(--accent-orange)" letter-spacing="2">
        <textPath href="#sloganArc" startOffset="50%" text-anchor="middle">使いやすい、見やすい、分かりやすい</textPath>
      </text>
    </svg>

    <div class="item-illust item-walker" role="img" aria-label="歩行器のイラスト"></div>
    <div class="item-illust item-cane" role="img" aria-label="杖のイラスト"></div>
    <div class="item-illust item-bed" role="img" aria-label="介護ベッドのイラスト"></div>
    <div class="item-illust item-wheelchair" role="img" aria-label="車いすのイラスト"></div>

    <p class="message message-lead">日常生活に支援が必要な方、<br>支援をする方へ</p>
    <p class="message anshin-row">
      <span class="anshin-char">あ</span><span class="anshin-char">ん</span><span class="anshin-char">し</span><span class="anshin-char">ん</span><span class="anshin-particle">を</span>
    </p>
    <p class="message message-close">お届けします。</p>
    <div class="people-illust" role="img" aria-label="笑顔の高齢者と介護者たちのイラスト"></div>
  </section>

  <footer class="maker">
    <span class="maker-mark"></span>
    <span class="maker-name">青葉医療器株式会社</span>
  </footer>
</main>
</body>
</html>
```